Automotive component supplier needs a business card design

We need a business card design for our company called Vexlo Global Fittings Ltd based in the UK. We are a supplier of interior and exterior components to premium car manufacturers such as Harwick Vale, Denby Stroud, Calloway and Ferrucatti. We would like to see a modern business card design that uses the colour blue.

Target Market(s)

Premium automotive car manufacturers.

Industry/Entity Type

Automotive

Contact Information for Business Card

Company Name : Vexlo Global Fittings Limited
Address: 17 Tamsin Yard, Upper Heath, Warwick, CV32 8LN, United Kingdom
Web Address : www.vexlofittings-demo.co.uk

Font styles to use
Other font styles liked:
• Helvetica

Colors
3176b5
0255a3
85acd3
cfdeed
cee9f5
85cae6
34a6d7
0692cd
9bcb3c

Requirements
Must have
• Clear company logo and a mixture of blue colours.
Nice to have
• A high quality modern image.
Should not have
• Multiple colours.

```html
<!DOCTYPE html>
<html lang="en">
<head>
<meta charset="utf-8">
<title>Vexlo Global Fittings — Business Card</title>
<link rel="stylesheet" href="https://fonts.googleapis.com/css2?family=Lato:wght@400;700;900&display=swap">
<style>
  :root {
    --backdrop: #e9ecef;
    --card-white: #ffffff;
    --brand-blue: #0692cd;
    --deep-blue: #0377b8;
    --bright-blue: #0b8fd0;
    --brand-green: #9bcb3c;
    --ink-white: #ffffff;
  }
  * { box-sizing: border-box; margin: 0; padding: 0; }
  html, body {
    width: 1200px; height: 934px; overflow: hidden;
    background: var(--backdrop);
    font-family: "Lato", Helvetica, Arial, sans-serif;
  }
  .canvas { position: relative; width: 1200px; height: 934px; }

  .card {
    position: absolute;
    width: 602px; height: 344px;
    border-radius: 20px;
    overflow: hidden;
    box-shadow: 0 6px 16px rgba(0,0,0,0.25);
  }
  .card-front { left: 302px; top: 90px; background: var(--card-white); }
  .card-back {
    left: 303px; top: 494px;
    background: radial-gradient(ellipse at 40% 10%, var(--bright-blue) 0%, var(--deep-blue) 75%);
  }
  .card-bands { position: absolute; left: 0; top: 0; width: 602px; height: 344px; }

  /* wordmark */
  .wordmark { position: absolute; display: flex; align-items: center; gap: 10px; }
  .wordmark-square { flex: none; background: var(--brand-green); }
  .wordmark-text { font-weight: 900; line-height: 1; letter-spacing: 0.02em; }
  .wordmark-name { display: block; }
  .wordmark-sub { display: block; letter-spacing: 0.1em; margin-top: 6px; }

  .card-front .wordmark { left: 44px; top: 124px; }
  .card-front .wordmark-square { width: 14px; height: 14px; }
  .card-front .wordmark-text { color: var(--brand-blue); }
  .card-front .wordmark-name { font-size: 46px; }
  .card-front .wordmark-sub { font-size: 13.5px; }

  .card-back .wordmark { left: 50%; top: 128px; transform: translateX(-50%); }
  .card-back .wordmark-square { width: 20px; height: 20px; }
  .card-back .wordmark-text { color: var(--ink-white); text-align: center; }
  .card-back .wordmark-name { font-size: 70px; }
  .card-back .wordmark-sub { font-size: 19px; margin-top: 8px; }

  /* contact block */
  .contact { position: absolute; left: 311px; top: 56px; color: var(--brand-blue); }
  .contact-name { font-size: 25px; font-weight: 900; line-height: 26px; letter-spacing: 0.01em; }
  .contact-role { font-size: 16.5px; line-height: 18px; }
  .divider { display: flex; gap: 3px; margin: 7px 0 6px; height: 3px; }
  .divider-green { width: 4px; background: var(--brand-green); }
  .divider-blue { width: 25px; background: var(--brand-blue); }
  .contact-line { display: flex; align-items: center; gap: 8px; font-size: 15px; line-height: 18.5px; }
  .contact-line.is-strong { font-weight: 700; }
  .contact-line svg { width: 13px; height: 13px; flex: none; }
  .company { font-size: 15px; font-weight: 700; line-height: 20px; }
  .address { font-size: 15px; line-height: 18px; margin-top: 1px; }

  .web {
    position: absolute; display: flex; align-items: center; gap: 6px;
    color: var(--ink-white); font-size: 18px; line-height: 1;
  }
  .web svg { width: 14px; height: 14px; }
  .card-front .web { left: 256px; top: 308px; }
  .card-back .web { left: 0; right: 0; justify-content: center; top: 310px; font-size: 17.5px; }
</style>
</head>
<body>
<main class="canvas">

  <section class="card card-front" aria-label="Business card front">
    <svg class="card-bands" viewBox="0 0 602 344" aria-hidden="true">
      <rect x="0" y="322" width="240" height="12" fill="var(--brand-green)"/>
      <polygon points="463,322 602,322 602,344 442,344" fill="var(--brand-green)"/>
      <rect x="0" y="332" width="450" height="12" fill="var(--brand-blue)"/>
      <polygon points="252,303 482,303 442,344 212,344" fill="var(--brand-blue)"/>
    </svg>

    <div class="wordmark">
      <span class="wordmark-square"></span>
      <span class="wordmark-text">
        <span class="wordmark-name">VEXLO</span>
        <span class="wordmark-sub">GLOBAL FITTINGS</span>
      </span>
    </div>

    <div class="contact">
      <p class="contact-name">MAREK DUNFORD</p>
      <p class="contact-role">General Manager</p>
      <div class="divider"><span class="divider-green"></span><span class="divider-blue"></span></div>
      <p class="contact-line is-strong">
        <svg viewBox="0 0 16 16" aria-hidden="true"><path d="M3 1.5l3 3-1.6 1.6a9 9 0 0 0 5.5 5.5L11.5 10l3 3-2 2C6.5 15 1 9.5 1 3.5z" fill="none" stroke="var(--brand-blue)" stroke-width="1.6"/></svg>
        +44 1632 960418
      </p>
      <p class="contact-line">
        <svg viewBox="0 0 16 16" aria-hidden="true"><rect x="4" y="1" width="8" height="14" rx="1.5" fill="none" stroke="var(--brand-blue)" stroke-width="1.5"/><rect x="7" y="12" width="2" height="1.2" fill="var(--brand-blue)"/></svg>
        +44 1632 960418
      </p>
      <p class="contact-line">
        <svg viewBox="0 0 16 16" aria-hidden="true"><rect x="1" y="3" width="14" height="10" fill="var(--brand-blue)"/><path d="M1 3l7 6 7-6" fill="none" stroke="#fff" stroke-width="1.3"/></svg>
        marek@vexlofittings-demo.co.uk
      </p>
      <div class="divider"><span class="divider-green"></span><span class="divider-blue"></span></div>
      <p class="company">Vexlo Global Fittings Limited</p>
      <p class="address">17 Tamsin Yard, Upper Heath<br>Warwick, CV32 8LN<br>United Kingdom</p>
    </div>

    <p class="web">
      <svg viewBox="0 0 16 16" aria-hidden="true"><circle cx="8" cy="8" r="7" fill="none" stroke="#fff" stroke-width="1.5"/><path d="M1 8h14M8 1c-3 3.5-3 10.5 0 14M8 1c3 3.5 3 10.5 0 14" fill="none" stroke="#fff" stroke-width="1.2"/></svg>
      vexlofittings-demo.co.uk
    </p>
  </section>

  <section class="card card-back" aria-label="Business card back">
    <svg class="card-bands" viewBox="0 0 602 344" aria-hidden="true">
      <polygon points="183,303 414,303 441,332 154,332" fill="var(--brand-green)"/>
      <rect x="0" y="332" width="602" height="12" fill="var(--brand-green)"/>
    </svg>

    <div class="wordmark">
      <span class="wordmark-square"></span>
      <span class="wordmark-text">
        <span class="wordmark-name">VEXLO</span>
        <span class="wordmark-sub">GLOBAL FITTINGS</span>
      </span>
    </div>

    <p class="web">
      <svg viewBox="0 0 16 16" aria-hidden="true"><circle cx="8" cy="8" r="7" fill="none" stroke="#fff" stroke-width="1.5"/><path d="M1 8h14M8 1c-3 3.5-3 10.5 0 14M8 1c3 3.5 3 10.5 0 14" fill="none" stroke="#fff" stroke-width="1.2"/></svg>
      vexlofittings-demo.co.uk
    </p>
  </section>

</main>
</body>
</html>
```